need to update our new address on letterhead and business cards. Also open to
a redesign and logo in the near future as we are changing our name. New address is Bramcote Commerce Court, 781 Ashgrove Street, Linwood Falls, CT 06287

Target Market(s)

35-75 yrs of age

Industry/Entity Type

Business

Requirements
Nice to have
• We are a financial firm so this need to look impressive and classy

```html
<!DOCTYPE html>
<html lang="en">
<head>
<meta charset="utf-8">
<title>Halvard Financial – Business Card</title>
<link href="https://fonts.googleapis.com/css2?family=Cormorant+Garamond:wght@500&family=Open+Sans:wght@400&family=Oswald:wght@400&display=swap" rel="stylesheet">
<style>
  :root {
    --stage: #3f679a;
    --stage-light: #4c78ad;
    --navy-deep: #0f2b57;
    --navy-mid: #1d4478;
    --navy-light: #2f5c94;
    --paper: #ffffff;
    --ink: #1c2f55;
    --ink-soft: #4a5670;
    --accent: #2a63c8;
  }
  * { margin: 0; padding: 0; box-sizing: border-box; }
  html, body { width: 1200px; height: 914px; overflow: hidden; }
  body {
    background: linear-gradient(180deg, var(--stage) 0%, var(--stage-light) 100%);
    position: relative;
  }
  .card {
    position: absolute;
    top: 180px;
    width: 310px;
    height: 542px;
    overflow: hidden;
  }
  .card--back { left: 250px; background: var(--paper); }
  .card--front {
    left: 640px;
    background: linear-gradient(180deg, var(--navy-deep) 0%, var(--navy-mid) 55%, var(--navy-light) 100%);
  }
  .wordmark {
    position: absolute;
    top: 150px;
    left: 0; right: 0;
    display: flex;
    align-items: center;
    gap: 10px;
  }
  .wordmark__rule { flex: 1; height: 1px; }
  .wordmark__name {
    font-family: "Cormorant Garamond", serif;
    font-weight: 500;
    font-size: 31px;
    letter-spacing: 0.5px;
    white-space: nowrap;
  }
  .card--back .wordmark__rule { background: var(--ink); }
  .card--back .wordmark__name { color: var(--ink); }
  .card--front .wordmark__rule { background: rgba(255,255,255,0.75); }
  .card--front .wordmark__name { color: #ffffff; }
  .holder {
    position: absolute;
    top: 300px; left: 0; right: 0;
    text-align: center;
    color: #ffffff;
  }
  .holder__name {
    font-family: "Oswald", sans-serif;
    font-size: 19px;
    letter-spacing: 0.3px;
  }
  .holder__title {
    font-family: "Open Sans", sans-serif;
    font-size: 13px;
    margin-top: 6px;
    color: #e3eaf5;
  }
  .contact {
    position: absolute;
    top: 225px;
    left: 36px; right: 24px;
    list-style: none;
    font-family: "Open Sans", sans-serif;
    font-size: 11.5px;
    color: var(--ink-soft);
    line-height: 1.55;
  }
  .contact li { display: flex; gap: 8px; margin-bottom: 8px; }
  .contact svg { flex: none; width: 12px; height: 12px; margin-top: 3px; }
  .tab {
    position: absolute;
    left: 50%;
    width: 34px; height: 10px;
    margin-left: -17px;
    background: var(--accent);
  }
  .card--back .tab { top: 0; }
  .card--front .tab { bottom: 0; }
</style>
</head>
<body>

  <section class="card card--back" aria-label="Business card, contact side">
    <span class="tab"></span>
    <div class="wordmark">
      <span class="wordmark__rule"></span>
      <span class="wordmark__name">Halvard Financial</span>
      <span class="wordmark__rule"></span>
    </div>
    <ul class="contact">
      <li>
        <svg viewBox="0 0 12 12" aria-hidden="true"><circle cx="6" cy="6" r="5.5" fill="#1c2f55"/><path d="M6 3a2 2 0 0 0-2 2c0 1.5 2 3.8 2 3.8S8 6.5 8 5a2 2 0 0 0-2-2z" fill="#fff"/></svg>
        <span>Bramcote Commerce Court, 781 Ashgrove Street, Linwood Falls, CT 06287</span>
      </li>
      <li>
        <svg viewBox="0 0 12 12" aria-hidden="true"><circle cx="6" cy="6" r="5.5" fill="#1c2f55"/><path d="M4 3.2l1.2 1.6-.6.8c.4.9 1 1.5 1.8 1.8l.8-.6 1.6 1.2-.6 1c-2.4-.2-4.6-2.4-4.8-4.8z" fill="#fff"/></svg>
        <span>555-210-0147 &nbsp;&#9632;&nbsp; Fax 555-210-0162</span>
      </li>
      <li>
        <svg viewBox="0 0 12 12" aria-hidden="true"><circle cx="6" cy="6" r="5.5" fill="#1c2f55"/><rect x="3.2" y="4" width="5.6" height="4" fill="none" stroke="#fff" stroke-width=".8"/><path d="M3.2 4L6 6.3 8.8 4" fill="none" stroke="#fff" stroke-width=".8"/></svg>
        <span>DAshworth@HalvardFinancialSvcs.com</span>
      </li>
      <li>
        <svg viewBox="0 0 12 12" aria-hidden="true"><circle cx="6" cy="6" r="5.5" fill="#1c2f55"/><circle cx="6" cy="6" r="3" fill="none" stroke="#fff" stroke-width=".7"/><path d="M3 6h6M6 3c-1.2 1.6-1.2 4.4 0 6M6 3c1.2 1.6 1.2 4.4 0 6" fill="none" stroke="#fff" stroke-width=".6"/></svg>
        <span>www.HalvardFinancialSvcs.com</span>
      </li>
    </ul>
  </section>

  <section class="card card--front" aria-label="Business card, name side">
    <div class="wordmark">
      <span class="wordmark__rule"></span>
      <span class="wordmark__name">Halvard Financial</span>
      <span class="wordmark__rule"></span>
    </div>
    <div class="holder">
      <p class="holder__name">Daniel R. Ashworth, Sr. RFC</p>
      <p class="holder__title">President/CEO</p>
    </div>
    <span class="tab"></span>
  </section>

</body>
</html>
```